Dentistry

Dentist's personal business card. No logo needed. The card shoul deliver the massage of reliability, professionalism, experience.
Please ad the full brief of the project: down the line it says: the winning look should be precise and pristine NO pictures of Teeth, smiles, instruments etc.

The details to be desplaid are:
Dr. Rob Valdoni
Doctor of Dental Surgery
PHD
Web. Www.drvaldoni.com
Email. Rob@drvaldoni.com
Tel 07731482590
Surgery address. 27Bharwick road London SW4 7QN UK
82 Fenwyn Row London SW3 2HT. Uk

Reason: Decided to make the payment unrefundable in order to get more designers involved.

Requirements
Should not have
• Logo, teeth, smile any sort of instruments.

```html
<!DOCTYPE html>
<html lang="en">
<head>
<meta charset="utf-8">
<title>Adam Hollis – Business Card</title>
<link rel="stylesheet" href="https://fonts.googleapis.com/css2?family=Source+Sans+3:wght@400&display=swap">
<style>
  :root {
    --ink: #0a0a0a;
    --accent: #1de6ef;
    --paper: #ffffff;
    --rim-light: #e6e6e6;
    --rim-dark: #5a5a5a;
  }
  * { margin: 0; padding: 0; box-sizing: border-box; }
  html, body {
    width: 1200px;
    height: 796px;
    overflow: hidden;
    background: var(--paper);
  }
  .card {
    position: relative;
    width: 1200px;
    height: 796px;
    background: var(--paper);
    font-family: "Source Sans 3", "Myriad Pro", Arial, sans-serif;
    font-weight: 400;
    color: var(--ink);
  }
  .card__text {
    position: absolute;
    left: 114px;
    line-height: 1;
    white-space: nowrap;
  }
  .card__name { top: 72px; font-size: 112px; letter-spacing: -1px; }
  .card__role { top: 184px; font-size: 83px; color: var(--accent); }
  .card__phone { left: 188px; font-size: 88px; }
  .card__phone--landline { top: 294px; }
  .card__phone--mobile { top: 372px; }
  .card__email { left: 188px; top: 456px; font-size: 64px; }
  .card__web { top: 591px; font-size: 53px; color: var(--accent); }

  .contact-icon {
    position: absolute;
    left: 110px;
    width: 54px;
    height: 54px;
  }
  .contact-icon--landline { top: 313px; }
  .contact-icon--mobile { top: 390px; }
  .contact-icon--email { top: 466px; }

  .trim-guides {
    position: absolute;
    inset: 0;
    pointer-events: none;
  }
</style>
</head>
<body>
<main class="card">
  <svg class="trim-guides" width="1200" height="796" viewBox="0 0 1200 796" aria-hidden="true">
    <g stroke="var(--accent)" stroke-width="2">
      <line x1="1062" y1="0" x2="1062" y2="796"/>
      <line x1="0" y1="712" x2="1200" y2="712"/>
      <line x1="0" y1="745" x2="1200" y2="745"/>
    </g>
  </svg>

  <h1 class="card__text card__name">Adam Hollis</h1>
  <p class="card__text card__role">Dental Practitioner</p>

  <svg class="contact-icon contact-icon--landline" viewBox="0 0 54 54" aria-hidden="true">
    <defs>
      <linearGradient id="rim" x1="0" y1="0" x2="1" y2="1">
        <stop offset="0" stop-color="var(--rim-light)"/>
        <stop offset="1" stop-color="var(--rim-dark)"/>
      </linearGradient>
    </defs>
    <circle cx="27" cy="27" r="26" fill="url(#rim)"/>
    <circle cx="27" cy="27" r="21" fill="var(--accent)"/>
    <path d="M18 17c2-2 4-2 5 0l2 4c1 2 0 3-1 4 1 3 3 5 6 6 1-1 2-2 4-1l4 2c2 1 2 3 0 5-3 3-8 2-13-3s-10-11-7-17z" fill="#fff"/>
  </svg>
  <p class="card__text card__phone card__phone--landline">01632 960418</p>

  <svg class="contact-icon contact-icon--mobile" viewBox="0 0 54 54" aria-hidden="true">
    <circle cx="27" cy="27" r="26" fill="url(#rim)"/>
    <circle cx="27" cy="27" r="21" fill="var(--accent)"/>
    <rect x="20" y="13" width="14" height="28" rx="2" fill="none" stroke="#fff" stroke-width="2"/>
    <rect x="22.5" y="16" width="9" height="9" fill="#fff"/>
    <g fill="#fff">
      <rect x="22.5" y="28" width="2.5" height="2"/><rect x="26" y="28" width="2.5" height="2"/><rect x="29.5" y="28" width="2.5" height="2"/>
      <rect x="22.5" y="32" width="2.5" height="2"/><rect x="26" y="32" width="2.5" height="2"/><rect x="29.5" y="32" width="2.5" height="2"/>
      <rect x="22.5" y="36" width="2.5" height="2"/><rect x="26" y="36" width="2.5" height="2"/><rect x="29.5" y="36" width="2.5" height="2"/>
    </g>
  </svg>
  <p class="card__text card__phone card__phone--mobile">07700 900362</p>

  <svg class="contact-icon contact-icon--email" viewBox="0 0 54 54" aria-hidden="true">
    <circle cx="27" cy="27" r="26" fill="url(#rim)"/>
    <circle cx="27" cy="27" r="21" fill="var(--accent)"/>
    <rect x="14" y="18" width="26" height="18" fill="none" stroke="#fff" stroke-width="2"/>
    <path d="M14 18l13 10 13-10M14 36l10-9M40 36l-10-9" fill="none" stroke="#fff" stroke-width="2"/>
  </svg>
  <p class="card__text card__email">contact@adamhollis.co.uk</p>

  <p class="card__text card__web">www.adamhollis.co.uk</p>
</main>
</body>
</html>
```